Design the best looking box truck wrap in town for an insulation and whole house fan contractor.

I would like to update my vehicle wrap look for Marlow Power Systems. Our main products are insulation and whole house fans.
I got my car wrapped recently and would like to adopt a similar look to it.

I thought it important to include a picture of my current wrap design and what I don’t like about it so as to show more what I’m looking for.
I’m looking for a more simple design.

Target Market(s)

High End Homeowners

Industry/Entity Type

Marlow power systems

Colors
0054AA
0677BA
7BADD7
CADEEF
E8F1F8
59FF00
82FF00
B8FF75
E3FFCB
F4FFEA

Requirements
Must have
• Logo as the Focal point. Insulation & Whole House fans. 482-316-9027 KRT5830196
Nice to have
• The logo as the focal point that stands out the most.
Should not have
• Pictures. Any services other than insulation and whole house fans

```html
<!DOCTYPE html>
<html lang="en">
<head>
<meta charset="utf-8">
<title>Marlow Power Systems – Box Truck Wrap</title>
<link rel="stylesheet" href="https://fonts.googleapis.com/css2?family=Michroma&family=Oswald:wght@600&family=Mr+Dafoe&display=swap">
<style>
  :root {
    --page-bg: #ffffff;
    --wrap-blue: #1746a8;
    --wrap-blue-light: #1f62d0;
    --green-dark: #49a61b;
    --green-mid: #5fb82a;
    --green-light: #8dcb48;
    --green-shadow: #2f7d12;
    --white: #ffffff;
  }
  html, body {
    margin: 0;
    padding: 0;
    width: 935px;
    height: 1200px;
    overflow: hidden;
    background: var(--page-bg);
  }
  .sheet {
    position: relative;
    width: 935px;
    height: 1200px;
  }
  .wrap-panel {
    position: absolute;
    left: 22px;
    top: 400px;
    width: 891px;
    height: 400px;
    display: block;
  }
  .brand-name {
    font-family: "Michroma", sans-serif;
    fill: var(--white);
    font-size: 54px;
  }
  .tagline {
    font-family: "Mr Dafoe", cursive;
    fill: var(--white);
    font-size: 60px;
  }
  .services {
    font-family: "Michroma", sans-serif;
    fill: var(--white);
    font-size: 25px;
  }
  .phone, .licence {
    font-family: "Oswald", sans-serif;
    font-weight: 600;
    fill: var(--white);
    stroke: var(--green-shadow);
    stroke-width: 4px;
    paint-order: stroke;
  }
  .phone { font-size: 50px; }
  .licence { font-size: 38px; }
</style>
</head>
<body>
<main class="sheet">
  <svg class="wrap-panel" viewBox="0 0 1620 727" xmlns="http://www.w3.org/2000/svg" aria-label="Box truck side wrap for Marlow Power Systems">
    <defs>
      <linearGradient id="green-field" x1="0" y1="0" x2="1" y2="0">
        <stop offset="0" stop-color="var(--green-dark)"/>
        <stop offset="0.6" stop-color="var(--green-mid)"/>
        <stop offset="1" stop-color="var(--green-light)"/>
      </linearGradient>
      <radialGradient id="blue-dots" cx="0.1" cy="0" r="0.9">
        <stop offset="0" stop-color="var(--wrap-blue-light)" stop-opacity="0.9"/>
        <stop offset="1" stop-color="var(--wrap-blue-light)" stop-opacity="0"/>
      </radialGradient>
      <radialGradient id="green-dots" cx="0.2" cy="0.5" r="0.8">
        <stop offset="0.4" stop-color="var(--green-dark)" stop-opacity="0.8"/>
        <stop offset="1" stop-color="var(--green-dark)" stop-opacity="0"/>
      </radialGradient>
    </defs>

    <!-- green background field -->
    <rect class="field-green" width="1620" height="727" fill="url(#green-field)"/>

    <!-- halftone accent on green side -->
    <path role="img" aria-label="Green halftone dot pattern" d="M1330,0 L1560,0 C1620,200 1600,450 1420,600 C1300,700 1100,727 900,727 L1200,727 C1400,600 1480,400 1450,200 C1440,100 1400,40 1330,0 Z" fill="url(#green-dots)"/>

    <!-- blue main panel with white edge -->
    <path class="panel-blue" d="M0,455 C250,600 500,668 720,665 C1100,658 1392,450 1386,193 C1383,95 1355,35 1315,0 L0,0 Z"
          fill="var(--wrap-blue)" stroke="var(--white)" stroke-width="12"/>
    <rect x="0" y="0" width="1620" height="6" fill="var(--wrap-blue)"/>

    <!-- halftone accent on blue side -->
    <path role="img" aria-label="Blue halftone dot pattern" d="M0,0 L510,0 C420,70 260,110 0,145 Z" fill="url(#blue-dots)"/>

    <!-- brand -->
    <circle class="brand-mark" cx="810" cy="170" r="50" fill="var(--green-mid)"/>
    <text class="brand-name" x="810" y="310" text-anchor="middle">MARLOW POWER</text>
    <text class="brand-name" x="810" y="370" text-anchor="middle">SYSTEMS</text>

    <text class="tagline" x="822" y="448" text-anchor="middle">Feel The Difference</text>
    <text class="services" x="810" y="545" text-anchor="middle">Insulation &amp; Whole House Fans</text>

    <!-- contact -->
    <g class="phone-icon" transform="translate(1212,598)" fill="none" stroke="var(--white)" stroke-width="3" stroke-linecap="round">
      <path d="M6,2 C0,8 0,22 6,30 L11,26 L8,19 L12,14 L10,6 Z"/>
      <path d="M16,10 C19,13 19,18 16,21"/>
    </g>
    <text class="phone" x="1538" y="633" text-anchor="end">482-316-9027</text>
    <text class="licence" x="1538" y="682" text-anchor="end">KRT5830196</text>
  </svg>
</main>
</body>
</html>
```